Paleo Diet Book Cover Design

I need a cover designed for my book Stone Frame that will be sold on Brightleaf Reader and other sites. So the front, side and back will need to be designed. I have attached part of the book here so feel free to skim through the content and give it a quick read to get a feel for what the book is about. Stone Frame is about eating the diet of the caveman (paleolithic era-paleo) and a 12 week workout plan with a grocery shopping list and meal plans. It is for men and women ages 18+ who are interested in health and fitness and becoming healthier overall.
The graphics should be secondary, and it should add to the text, not distract from it. This is even more important because the size of the cover displayed on Brightleaf/Reader, when your book is first seen by a potential buyer, is so tiny. It's barely an inch high, and even smaller in width.
So the words have to be big, bold, benefit-rich and easy to read. That also means, don't mess with the fancy fonts. Clean, clear, crisp font is best. And, did I say BIG already?
Contrast the colors of the text and background, so its even easier to read. That means, dark text on light background or visa versa. Colors like darker reds, blues / teals and oranges.
Please read this: http://www.jacketforge.net/8-cover-design-secrets-publishers-use-to-manipulate-readers-into-buying-books/
The cover has to be bold and easy to read, it has to stick out, it has to draw the attention of your readers so that they zero in on my book, out of all the other books on the page. (Much like they would when viewing a classified ads site/page.)
The Title of the Book is Stone Frame, and the subtitle is "Transform Your Body For Life in 12 Weeks With Proven Workouts and Paleo Diet Based Nutrition" Perhaps “Transform Your Body For Life in 12 Weeks” could also be in a large font similar to the title with the rest of the subtitle following afterwards. You can try having the title be the smaller font with the subtitle being the larger font as well.
Then the authors name "Martin Oakes” incorporated into the design.
I am not sure what to use as the background type of design for the front of the book so feel free to be creative with that.
The size needs to be 1563 pixels on the shortest side and 2500 pixels on the longest side just for the front of the cover.

```html
<!DOCTYPE html>
<html lang="en">
<head>
<meta charset="utf-8">
<title>Stone Frame — Book Cover</title>
<link rel="stylesheet" href="https://fonts.googleapis.com/css2?family=Oswald:wght@600&family=Open+Sans:wght@700;800&display=swap">
<style>
  :root {
    --cover-red: #d8151d;
    --cover-red-deep: #a80d14;
    --title-gold: #fcc232;
    --title-orange: #f3951c;
    --subtitle-peach: #f8c48a;
    --author-band: #4a3f9d;
    --author-text: #ffffff;
    --photo-dark: #3a3d44;
    --photo-light: #9aa3ad;
    --figure-tone: #e9b49a;
    --plate-tone: #f4f1ec;
  }
  html, body {
    margin: 0;
    padding: 0;
    width: 750px;
    height: 1200px;
    overflow: hidden;
    background: var(--cover-red);
  }
  .book-cover {
    display: block;
    width: 750px;
    height: 1200px;
  }
  .cover-title {
    font-family: "Oswald", "Arial Narrow", sans-serif;
    font-weight: 600;
  }
  .cover-subtitle {
    font-family: "Open Sans", Arial, sans-serif;
    font-weight: 700;
    fill: var(--subtitle-peach);
  }
  .cover-author {
    font-family: "Open Sans", Arial, sans-serif;
    font-weight: 700;
    fill: var(--author-text);
  }
</style>
</head>
<body>
<svg class="book-cover" viewBox="0 0 750 1200" xmlns="http://www.w3.org/2000/svg">
  <defs>
    <radialGradient id="red-field" cx="50%" cy="45%" r="70%">
      <stop offset="0" stop-color="var(--cover-red)"/>
      <stop offset="1" stop-color="var(--cover-red-deep)"/>
    </radialGradient>
    <linearGradient id="title-fill" x1="0" y1="0" x2="0" y2="1">
      <stop offset="0" stop-color="var(--title-gold)"/>
      <stop offset="1" stop-color="var(--title-orange)"/>
    </linearGradient>
    <linearGradient id="gym-photo" x1="0" y1="0" x2="1" y2="0">
      <stop offset="0" stop-color="var(--photo-dark)"/>
      <stop offset="0.5" stop-color="var(--photo-light)"/>
      <stop offset="1" stop-color="var(--photo-dark)"/>
    </linearGradient>
    <radialGradient id="figure-glow" cx="50%" cy="50%" r="50%">
      <stop offset="0" stop-color="var(--figure-tone)" stop-opacity="0.45"/>
      <stop offset="0.7" stop-color="var(--plate-tone)" stop-opacity="0.18"/>
      <stop offset="1" stop-color="var(--plate-tone)" stop-opacity="0"/>
    </radialGradient>
  </defs>

  <rect class="title-field" x="0" y="272" width="750" height="795" fill="url(#red-field)"/>

  <rect class="hero-photo" x="0" y="0" width="750" height="272" fill="url(#gym-photo)"
        role="img" aria-label="Photo of two fit people in a gym lifting dumbbells"/>

  <ellipse class="hero-figure" cx="310" cy="720" rx="200" ry="180" fill="url(#figure-glow)"
           role="img" aria-label="Illustration of a smiling woman holding a bathroom scale above a plate of fruit, vegetables and meat"/>

  <g class="cover-title" fill="url(#title-fill)">
    <text x="65" y="568" font-size="342" textLength="626" lengthAdjust="spacingAndGlyphs">STONE</text>
    <text x="65" y="878" font-size="342" textLength="626" lengthAdjust="spacingAndGlyphs">FRAME</text>
  </g>

  <text class="cover-subtitle" x="375" y="953" font-size="43" text-anchor="middle" textLength="626" lengthAdjust="spacingAndGlyphs">TRANSFORM YOUR BODY</text>
  <text class="cover-subtitle" x="63" y="1033" font-size="43" textLength="276" lengthAdjust="spacingAndGlyphs">FOR LIFE IN</text>
  <text class="cover-subtitle" x="348" y="1033" font-size="62" textLength="328" lengthAdjust="spacingAndGlyphs">12 WEEKS</text>

  <rect class="author-band" x="0" y="1067" width="750" height="133" fill="var(--author-band)"/>
  <text class="cover-author" x="375" y="1158" font-size="74" text-anchor="middle">Martin Oakes</text>
</svg>
</body>
</html>
```